Letterhead for sustainable Last Mile Logistics needed

Dear all,

we are looking for a powerful design for our letterhead. We are a Berlin-based (Germany) logistics company which delivers parcel on the last mile in a sustainable way. Design should communicate: sustainability, integrity, one family, performance-focused, passionate for excellence and customer experience. Please find company logo attached.

Looking forward for

```html
<!DOCTYPE html>
<html lang="en">
<head>
<meta charset="utf-8">
<title>Greenway Parcel Letterhead</title>
<link rel="stylesheet" href="https://fonts.googleapis.com/css2?family=Arimo:wght@400&family=Open+Sans:wght@400;700&display=swap">
<style>
  :root {
    --paper: #f6f4f5;
    --brand-green: #2f9e48;
    --text-body: #4a4a4a;
    --text-heading: #555555;
    --text-contact: #222222;
    --ink: #1f2733;
  }
  html, body {
    margin: 0;
    padding: 0;
    overflow: hidden;
  }
  body {
    width: 935px;
    height: 1200px;
    background: var(--paper);
  }
  .letterhead {
    position: relative;
    width: 935px;
    height: 1200px;
    background: var(--paper);
    font-family: "Arimo", Arial, sans-serif;
    color: var(--text-body);
  }
  .brand {
    position: absolute;
    left: 89px;
    top: 150px;
    display: flex;
    align-items: center;
    gap: 10px;
  }
  .brand-dot {
    width: 22px;
    height: 22px;
    border-radius: 50%;
    background: var(--brand-green);
  }
  .brand-name {
    font-family: "Open Sans", Arial, sans-serif;
    font-weight: 700;
    font-size: 24px;
    letter-spacing: 0.5px;
    color: var(--brand-green);
  }
  .contact {
    position: absolute;
    left: 667px;
    top: 82px;
    font-family: "Open Sans", Arial, sans-serif;
    font-size: 15px;
    line-height: 18px;
    color: var(--text-contact);
  }
  .contact-address { margin: 0 0 10px; }
  .contact-line {
    display: flex;
    align-items: center;
    gap: 7px;
  }
  .contact-icon {
    width: 12px;
    height: 12px;
    fill: var(--brand-green);
    flex: none;
  }
  .greeting {
    position: absolute;
    left: 93px;
    top: 306px;
    margin: 0;
    font-weight: 400;
    font-size: 25px;
    color: var(--text-heading);
  }
  .letter-body {
    position: absolute;
    left: 93px;
    top: 377px;
    width: 753px;
    font-size: 14.6px;
    line-height: 20.5px;
    text-align: justify;
    hyphens: auto;
  }
  .letter-body p { margin: 0 0 20px; }
  .closing {
    position: absolute;
    left: 93px;
    top: 828px;
    margin: 0;
    font-size: 14.6px;
  }
  .signature {
    position: absolute;
    left: 89px;
    top: 860px;
    width: 124px;
    height: 44px;
    background: linear-gradient(90deg, rgba(31,39,51,0.15), rgba(31,39,51,0.35), rgba(31,39,51,0.1));
    border-radius: 4px;
  }
  .signer-name {
    position: absolute;
    left: 96px;
    top: 924px;
    margin: 0;
    font-size: 20px;
    color: var(--text-heading);
  }
  .signer-title {
    position: absolute;
    left: 96px;
    top: 951px;
    margin: 0;
    font-size: 16px;
    color: var(--text-body);
  }
</style>
</head>
<body>
<main class="letterhead">
  <header>
    <div class="brand">
      <span class="brand-dot"></span>
      <span class="brand-name">GREENWAY PARCEL</span>
    </div>
    <address class="contact" style="font-style: normal;">
      <p class="contact-address">Veldstraat 12B, 5062 KP<br>Heideveen, Nederland</p>
      <div class="contact-line">
        <svg class="contact-icon" viewBox="0 0 12 12" aria-hidden="true"><path d="M2.4 0.5 L4.3 2.8 L3.3 4.3 Q4.6 6.9 7.7 8.7 L9.2 7.7 L11.5 9.6 L10 11.5 Q4.5 10.8 0.5 2 Z"/></svg>
        <span>+ 31 (085) 000 4821</span>
      </div>
      <div class="contact-line">
        <svg class="contact-icon" viewBox="0 0 12 12" aria-hidden="true"><path d="M0.5 2.5 H11.5 V9.5 H0.5 Z M1 3 L6 6.6 L11 3" stroke="#f6f4f5" stroke-width="0.9"/></svg>
        <span>info@GREENWAYPARCEL.nl</span>
      </div>
      <div class="contact-line">
        <svg class="contact-icon" viewBox="0 0 12 12" aria-hidden="true"><circle cx="6" cy="6" r="5.5"/><path d="M0.5 6 H11.5 M6 0.5 Q3 6 6 11.5 M6 0.5 Q9 6 6 11.5" stroke="#f6f4f5" stroke-width="0.8" fill="none"/></svg>
        <span>www.GREENWAYPARCEL.nl</span>
      </div>
    </address>
  </header>

  <h1 class="greeting">Dear Mr. Harlow,</h1>

  <section class="letter-body">
    <p>Lorem ipsum dolor sit amet, consectetur adipiscing elit. Donec orci purus, luctus vitae dignissim eu, iaculis sed purus. Vivamus faucibus, ipsum nec aliquet viverra, leo mauris condimentum ligula, sit amet sagittis enim ligula quis arcu. Nam egestas tortor id nisi porttitor mattis. In tortor ante, ultricies in suscipit a, tempus non massa. Vivamus et auctor mi. Fusce vel massa nulla. Phasellus nec eros mauris, et scelerisque orci.</p>
    <p>Donec malesuada orci vitae nulla accumsan porta a id massa. Quisque accumsan iaculis magna sit amet fringilla. Maecenas consequat, magna eget tincidunt semper, odio nibh rutrum mi, id feugiat ante nisi eu risus. Vestibulum nunc orci, rhoncus a placerat in, ultricies in mi. Cras mattis varius eros, vel fringilla nisi suscipit eget. Quisque scelerisque sagittis nulla at porttitor.</p>
    <p>Sed id augue vitae urna euismod commodo aliquet a quam. Pellentesque arcu velit, cursus et malesuada ut, consequat et diam. Nullam erat sem, rhoncus id ullamcorper vitae, rhoncus et arcu. In ultricies ultricies nulla, ut rutrum nisi iaculis at. Donec eu magna a metus ornare faucibus. Fusce aliquet faucibus ultricies. Morbi semper, est id tincidunt gravida, sem arcu adipiscing lacus, ac bibendum nulla leo eu purus. Quisque nec diam sed risus consectetur a ccumsan quis quis nibh. Vestibulum id purus lorem.</p>
    <p>It is a long established fact that a reader will be distracted by the readable content of a page when looking at its layout. The point of using Lorem Ipsum is that it has a more-or-less normal distribution of letters, as opposed to using 'Content here, content here', making it look like readable English. Many desktop publishing packages</p>
  </section>

  <p class="closing">Sincerely,</p>
  <div class="signature" role="img" aria-label="Handwritten signature of Daniel Harlow"></div>
  <p class="signer-name">Daniel Harlow</p>
  <p class="signer-title">CEO/ Founder</p>
</main>
</body>
</html>
```